A4 Desktop sign for Excess Luggage

We need a design for a desktop sign that will go in hotels offering a excess luggage service.
The sign will need to have the company logo(Vantrelo Worldwide) be in colours red white and blue.
Have the local outlet name address phone number and opening times. And also the fact we can do
letters parcels cargo and Excess luggage
highlighting for hotels that we do excess luggage
Industry/Entity Type
It Company

```html
<!DOCTYPE html>
<html lang="en">
<head>
<meta charset="utf-8">
<title>Vantrelo Worldwide – Excess Luggage Desk Sign</title>
<link href="https://fonts.googleapis.com/css2?family=Arimo:wght@400;700&display=swap" rel="stylesheet">
<style>
  :root {
    --red: #ee1c25;
    --blue: #1f4e9c;
    --navy: #1d3f8a;
    --white: #ffffff;
    --bag-teal: #3fa9d6;
    --bag-olive: #7a8a3a;
    --bag-brown: #7a4a3c;
    --bag-orange: #f39a1e;
  }
  * { box-sizing: border-box; margin: 0; padding: 0; }
  html, body { width: 851px; height: 1200px; overflow: hidden; background: var(--white); }
  .sign {
    position: relative;
    width: 851px;
    height: 1200px;
    background: var(--white);
    border: 8px solid var(--red);
    font-family: "Arimo", Arial, sans-serif;
    overflow: hidden;
  }
  .services-kicker {
    position: absolute;
    top: 108px; left: 0; width: 100%;
    text-align: center;
    color: var(--blue);
    font-weight: 700;
    font-size: 42px;
    letter-spacing: 0.5px;
    white-space: nowrap;
  }
  .headline-band {
    position: absolute;
    top: 156px; left: 0; width: 100%; height: 104px;
    background: var(--red);
    display: flex; align-items: center; justify-content: center;
  }
  .headline {
    color: var(--white);
    font-weight: 700;
    font-size: 71px;
    letter-spacing: 0.5px;
    white-space: nowrap;
  }
  .luggage-illustration {
    position: absolute;
    top: 322px; left: 168px; width: 550px; height: 380px;
    border-radius: 12px;
    background: linear-gradient(90deg, var(--bag-teal) 0%, var(--bag-olive) 35%, var(--bag-brown) 60%, var(--bag-orange) 100%);
    opacity: 0.85;
  }
  .outlet {
    position: absolute;
    left: 0; width: 100%;
    text-align: center;
    line-height: 1;
    white-space: nowrap;
  }
  .outlet-name { top: 756px; color: var(--red); font-weight: 700; font-size: 34px; }
  .outlet-hours { top: 799px; color: var(--blue); font-size: 37px; }
  .outlet-phone { top: 844px; color: var(--red); font-size: 38px; }
  .rule { position: absolute; left: 34px; width: 767px; }
  .rule-top { top: 913px; }
  .rule-bottom { top: 1015px; }
  .service-list {
    position: absolute;
    top: 929px; left: 0; width: 100%;
    text-align: center;
    color: var(--blue);
    font-size: 20px;
    line-height: 26px;
  }
  .service-list p { white-space: nowrap; }
  .service-list .sep { color: var(--red); padding: 0 2px; }
  .brand {
    position: absolute;
    top: 1066px; left: 0; width: 100%;
    display: flex; align-items: center; justify-content: center; gap: 16px;
  }
  .brand-mark { width: 40px; height: 40px; background: var(--red); }
  .brand-name {
    color: var(--navy);
    font-weight: 700;
    font-size: 44px;
    letter-spacing: -0.5px;
    white-space: nowrap;
  }
</style>
</head>
<body>
<main class="sign">
  <p class="services-kicker">LETTERS PARCELS CARGO AND</p>
  <div class="headline-band"><h1 class="headline">EXCESS LUGGAGE!</h1></div>

  <div class="luggage-illustration" role="img" aria-label="Illustration of a stack of colourful suitcases and travel bags"></div>

  <p class="outlet outlet-name">LOCAL OUTLET NAME HERE</p>
  <p class="outlet outlet-hours">Open time: 9.30</p>
  <p class="outlet outlet-phone">Tel: 020 7946 0381</p>

  <svg class="rule rule-top" height="6" viewBox="0 0 767 6" preserveAspectRatio="none"><path d="M0 3 Q383 0 767 3 Q383 6 0 3Z" fill="var(--blue)"/></svg>
  <div class="service-list">
    <p><span class="sep">|</span> Crown Post <span class="sep">|</span> Parcel Line <span class="sep">|</span> DKX <span class="sep">|</span> TRX <span class="sep">|</span> Fedra <span class="sep">|</span> Mail Consolidators <span class="sep">|</span></p>
    <p><span class="sep">|</span>Excess Baggage <span class="sep">|</span> Door to Door <span class="sep">|</span> Half and Full Pallets <span class="sep">|</span></p>
    <p><span class="sep">|</span> Exports and Imports <span class="sep">|</span> Container Shipping <span class="sep">|</span> Air Cargo <span class="sep">|</span> Customs Clearance</p>
  </div>
  <svg class="rule rule-bottom" height="6" viewBox="0 0 767 6" preserveAspectRatio="none"><path d="M0 3 Q383 0 767 3 Q383 6 0 3Z" fill="var(--blue)"/></svg>

  <div class="brand">
    <span class="brand-mark"></span>
    <span class="brand-name">Vantrelo Worldwide</span>
  </div>
</main>
</body>
</html>
```